Business Card Design Project

We need a business card for our new business based in Vancouver called
"Lumora" We are looking for a simple yet bold design for our business cards that will enable us to stand out from the pack. All business card details will be provided in the handover stage.
Updates

Thank you to all who have submitted

The work is great for the most part
Cards with creative use of the logo
have been more successful so far

Dark cards and rounded edges 
are also getting good reviews

Double sided is an option we would like to see explored

Thank you

Target Market(s)

Our clients are stressed business people, yoga/meditation enthusiast, and people looking for a new experience in a Spa enviroment

Industry/Entity Type

Business

Font styles to use
Other font styles liked:
• please check design file

Requirements
Must have
• Lumora

5218 E Kestrel Row, Vancouver, BC V5N 4K7

lumora@calmhaven.ca
Nice to have
• Creative approach to layout and design

Outside of the box design elements
Should not have
• Should not be too busy

```html
<!DOCTYPE html>
<html lang="en">
<head>
<meta charset="utf-8">
<title>Lumora – Business Card</title>
<link rel="stylesheet" href="https://fonts.googleapis.com/css2?family=Lato:wght@700&display=swap">
<style>
  :root {
    --card-bg: #ffffff;
    --brand-blue: #2b2ee6;
    --band-blue: #4a55f6;
    --band-edge: #2f32e4;
    --band-text: #ffffff;
  }
  html, body {
    margin: 0;
    padding: 0;
    width: 1200px;
    height: 686px;
    overflow: hidden;
    background: var(--card-bg);
  }
  .business-card {
    position: relative;
    width: 1200px;
    height: 686px;
    background: var(--card-bg);
    overflow: hidden;
  }
  .brand {
    position: absolute;
    left: 0;
    right: 0;
    top: 210px;
    height: 110px;
    display: flex;
    align-items: center;
    justify-content: center;
    gap: 34px;
  }
  .brand-dot {
    width: 84px;
    height: 84px;
    border-radius: 50%;
    background: var(--brand-blue);
    flex: none;
  }
  .brand-name {
    margin: 0;
    font-family: "Lato", sans-serif;
    font-weight: 700;
    font-size: 110px;
    line-height: 1;
    color: var(--brand-blue);
    white-space: nowrap;
  }
  .contact-band {
    position: absolute;
    left: 0;
    right: 0;
    top: 509px;
    bottom: 0;
    background: var(--band-blue);
    border-top: 3px solid var(--band-edge);
    display: flex;
    flex-direction: column;
    align-items: center;
    justify-content: center;
    padding-bottom: 28px;
    box-sizing: border-box;
  }
  .contact-line {
    margin: 0;
    font-family: "Lato", sans-serif;
    font-weight: 700;
    font-size: 38px;
    line-height: 48px;
    color: var(--band-text);
    white-space: nowrap;
  }
</style>
</head>
<body>
  <main class="business-card">
    <div class="brand">
      <span class="brand-dot" aria-hidden="true"></span>
      <h1 class="brand-name">Lumora</h1>
    </div>
    <footer class="contact-band">
      <p class="contact-line">5218 E Kestrel Row, Vancouver, BC V5N 4K7</p>
      <p class="contact-line">lumora@calmhaven.ca</p>
    </footer>
  </main>
</body>
</html>
```